Business Card Design- Mortgage Firm

Looking to design a business Card for our Outside sales people. This card is used to provide their contact information to prospective clients and realtors. Must have All Pertinent company and licensing information by law. We are looking for a very modern design that flows with our current logo color scheme. Red/White/Black

Industry/Entity Type

Mortgage Lender

Contact Information for Business Card

Must stick with current color scheme.

Colors
f04a50
ffffff
ecf7fb

Requirements
Must have
• Company Logo or similar
• Company Address (547 W Larkin Avenue, Suite 318, Corona CA 92877 NMLS: 2947163)
• Agent Name (Nora Pell)
• Title (Senior Mortgage Loan Originator)
• NMLS# 7395281
• Toll Free: 800-627-3184
• Direct : 310-555-8347
Nice to have
• Room for Agent Picture

```html
<!DOCTYPE html>
<html lang="en">
<head>
<meta charset="utf-8">
<title>Halvern Lending – Business Card</title>
<link rel="stylesheet" href="https://fonts.googleapis.com/css2?family=Open+Sans:wght@400;600;700;800&display=swap">
<style>
  :root {
    --ink: #000000;
    --panel: #060606;
    --brand-red: #b8232b;
    --accent-red: #f2141c;
    --bright-red: #ff1a1a;
    --mid-red: #d40008;
    --deep-red: #9a0008;
    --muted: #262626;
    --white: #ffffff;
  }
  * { margin: 0; padding: 0; box-sizing: border-box; }
  html, body { width: 1200px; height: 720px; overflow: hidden; background: var(--ink); }
  .card {
    position: relative;
    width: 1200px;
    height: 720px;
    background: var(--ink);
    font-family: "Open Sans", Arial, sans-serif;
    color: var(--white);
    overflow: hidden;
  }
  .card-sweep { position: absolute; inset: 0; }
  .brand-mark {
    position: absolute;
    left: 70px;
    top: 98px;
    width: 108px;
    height: 108px;
    background: var(--brand-red);
  }
  .brand-name {
    position: absolute;
    left: 208px;
    top: 80px;
    font-weight: 600;
    font-size: 74px;
    letter-spacing: 4px;
    color: var(--brand-red);
    line-height: 1;
  }
  .brand-tagline {
    position: absolute;
    left: 212px;
    top: 184px;
    width: 370px;
    font-weight: 700;
    font-size: 21px;
    letter-spacing: 22px;
    color: var(--muted);
    line-height: 1;
    white-space: nowrap;
  }
  .job-title {
    position: absolute;
    left: 83px;
    top: 315px;
    font-weight: 700;
    font-size: 27px;
    letter-spacing: 0.3px;
  }
  .agent {
    position: absolute;
    left: 750px;
    top: 306px;
    width: 300px;
    text-align: center;
    color: var(--accent-red);
  }
  .agent-name { font-weight: 800; font-size: 50px; line-height: 1.05; white-space: nowrap; }
  .agent-label { font-weight: 400; font-size: 30px; line-height: 1.1; }
  .license {
    position: absolute;
    left: 166px;
    top: 455px;
    font-size: 31px;
    font-weight: 400;
  }
  .contact-line {
    position: absolute;
    left: 154px;
    font-size: 26px;
    font-weight: 400;
    white-space: nowrap;
  }
  .contact-line.toll { top: 521px; }
  .contact-line.direct { top: 568px; }
  .contact-line.address { top: 614px; }
  .icon { position: absolute; left: 70px; width: 52px; height: 52px; }
  .icon.phone { top: 531px; }
  .icon.pin { top: 604px; }
</style>
</head>
<body>
<main class="card">
  <svg class="card-sweep" width="1200" height="720" viewBox="0 0 1200 720" aria-hidden="true">
    <defs>
      <linearGradient id="sweepShade" x1="0" y1="0" x2="0" y2="1">
        <stop offset="0" stop-color="#ff1a1a"/>
        <stop offset="0.55" stop-color="#c8000a"/>
        <stop offset="1" stop-color="#8a0006"/>
      </linearGradient>
    </defs>
    <path d="M738 101 C 655 240, 650 470, 752 600 L 790 600 C 705 470, 705 250, 786 101 Z" fill="url(#sweepShade)"/>
    <path d="M786 101 C 705 250, 705 470, 790 600 L 1200 600 L 1200 0 L 860 0 Z" fill="var(--panel)"/>
    <rect x="779" y="595" width="133" height="75" fill="var(--bright-red)"/>
    <rect x="912" y="595" width="139" height="75" fill="var(--mid-red)"/>
    <rect x="1051" y="595" width="149" height="75" fill="var(--deep-red)"/>
  </svg>

  <div class="brand-mark"></div>
  <div class="brand-name">HALVERN</div>
  <div class="brand-tagline">LENDING</div>

  <div class="job-title">SENIOR MORTGAGE LOAN ORIGINATOR</div>

  <div class="agent">
    <div class="agent-name">NORA PELL</div>
    <div class="agent-label">Agent Name</div>
  </div>

  <div class="license">NMLS# 7395281</div>

  <svg class="icon phone" viewBox="0 0 52 52" aria-hidden="true">
    <circle cx="26" cy="26" r="26" fill="var(--brand-red)"/>
    <path d="M18 14 l5 -1 l3 7 l-3 3 c2 4 4 6 8 8 l3 -3 l7 3 l-1 5 c-12 1 -23 -10 -22 -22 z" fill="var(--ink)"/>
  </svg>
  <div class="contact-line toll">Toll Free: 800-627-3184</div>
  <div class="contact-line direct">Direct : 310-555-8347</div>

  <svg class="icon pin" viewBox="0 0 52 52" aria-hidden="true">
    <circle cx="26" cy="26" r="26" fill="var(--brand-red)"/>
    <path d="M26 13 c-6 0 -10 4 -10 10 c0 7 10 17 10 17 s10 -10 10 -17 c0 -6 -4 -10 -10 -10 z" fill="var(--ink)"/>
    <circle cx="26" cy="23" r="3.5" fill="var(--brand-red)"/>
  </svg>
  <div class="contact-line address">547 W Larkin Avenue, Suite 318, Brenton CA 92877 NMLS: 2947163</div>
</main>
</body>
</html>
```